Brightmoor Notes To Do List

I am looking to design a new "Study To Do List" for High School students (Ages 15 - 18) . This will be printed as an A4 notepad and so should only be a single A4 page.

The Design will need to be professional and look semi-serious but also be appealing to High school students (Ages 15 - 18) and should NOT be gender specific.

I have attached a word document outlining the structure of the page. The space provided should be large enough that people can write in it comfortably.

The notepad will most likely be printed in black and white but I'm also looking at coloured options - colours should be kept to a minimum.

This will be printed professionally and should also include a 3mm bleed.

The design should also include the business logo (included in the word document)

Target Market(s)

High School students (Ages 15 - 18). Both genders

Industry/Entity Type

Education

Font styles to use
Serif
Sans Serif

Requirements
Must have
• Please see the word document attached.
Should not have
• Too much colour

```html
<!DOCTYPE html>
<html lang="en">
<head>
<meta charset="utf-8">
<title>Brightmoor Notes – Study To Do List</title>
<link rel="stylesheet" href="https://fonts.googleapis.com/css2?family=Open+Sans:wght@400;600;700&display=swap">
<style>
  :root{
    --navy:#233a52;
    --orange:#f47b16;
    --grey-band:#b3b3b3;
    --backdrop:#858585;
    --rule:#8a8a8a;
    --ink:#2b2b2b;
    --ink-soft:#777;
    --icon:#5a5a5a;
    --paper:#ffffff;
  }
  *{box-sizing:border-box;margin:0;padding:0}
  html,body{width:1200px;height:1200px;overflow:hidden;background:var(--backdrop)}
  body{font-family:"Open Sans",Arial,sans-serif;color:var(--ink);position:relative}
  .page{position:absolute;left:206px;top:42px;width:786px;height:1112px;background:var(--paper);overflow:hidden}
  .masthead{position:absolute;left:0;top:0;width:786px;height:96px;background:var(--navy)}
  .masthead-strip{position:absolute;left:0;top:96px;width:786px;height:14px;background:var(--grey-band)}
  .brand{position:absolute;left:52px;top:20px;width:68px;height:68px;border-radius:50%;background:var(--paper);
    display:flex;align-items:center;justify-content:center;text-align:center;
    font-weight:700;font-size:11px;line-height:1.15;color:var(--navy)}
  .title-rule{position:absolute;top:51px;height:2px;width:125px;background:#8a99a8}
  .title{position:absolute;left:300px;width:252px;top:44px;text-align:center;color:#fff;font-weight:700;font-size:26px;line-height:36px;white-space:nowrap}
  .date{position:absolute;right:26px;top:135px;font-size:14px;color:var(--ink)}
  .heading{position:absolute;left:28px;display:flex;align-items:center;gap:6px;font-weight:700;font-size:17px;color:var(--ink);height:22px}
  .heading svg{width:21px;height:21px}
  .rule{position:absolute;height:2px;background:var(--rule)}
  .vrule{position:absolute;width:2px;background:var(--rule)}
  .cell{position:absolute;font-size:13.5px;height:20px;line-height:20px}
  .band{position:absolute;left:28px;width:731px;height:7px;background:var(--navy)}
  .band i{position:absolute;top:0;height:7px;background:var(--orange)}
  .row{position:absolute;left:51px;width:708px;height:20px;display:flex;align-items:flex-end;font-size:13.5px;line-height:20px}
  .row .fill{flex:1;border-bottom:2px dotted #555;margin:0 0 5px 4px}
  .row.soft{color:var(--ink-soft)}
  .row .due{margin-left:4px}
  .row .fill.short{flex:0 0 290px}
</style>
</head>
<body>
<main class="page">
  <header>
    <div class="masthead"></div>
    <div class="masthead-strip"></div>
    <div class="brand">Brightmoor<br>Notes</div>
    <div class="title-rule" style="left:167px"></div>
    <div class="title-rule" style="left:562px"></div>
    <h1 class="title">STUDY TO DO LIST</h1>
  </header>

  <p class="date">Date: ........... / ............ / .........</p>

  <h2 class="heading" style="top:157px">
    <svg viewBox="0 0 20 20"><circle cx="10" cy="10" r="10" fill="var(--icon)"/><path d="M6 14l1-3 6-6 2 2-6 6z" fill="#fff"/></svg>REVISION
  </h2>
  <div class="rule" style="left:30px;width:728px;top:182px"></div>
  <div class="rule" style="left:30px;width:728px;top:207px"></div>
  <div class="rule" style="left:30px;width:728px;top:232px"></div>
  <div class="rule" style="left:30px;width:728px;top:257px"></div>
  <div class="rule" style="left:30px;width:728px;top:282px"></div>
  <div class="vrule" style="left:393px;top:182px;height:102px"></div>
  <span class="cell" style="left:39px;top:185px">1.</span>
  <span class="cell" style="left:39px;top:210px">2.</span>
  <span class="cell" style="left:39px;top:235px">3.</span>
  <span class="cell" style="left:39px;top:259px">4.</span>
  <span class="cell" style="left:402px;top:185px">5.</span>
  <span class="cell" style="left:402px;top:210px">6.</span>
  <span class="cell" style="left:402px;top:235px">7.</span>
  <span class="cell" style="left:402px;top:259px">8.</span>

  <div class="band" style="top:296px"><i style="left:0;width:124px"></i></div>

  <h2 class="heading" style="top:304px">
    <svg viewBox="0 0 20 20"><circle cx="10" cy="10" r="10" fill="var(--icon)"/><path d="M5 10l5-4.5 5 4.5v5H5z" fill="#fff"/><rect x="8.5" y="11" width="3" height="4" fill="var(--icon)"/></svg>HOMEWORK
  </h2>
  <div class="row" style="top:330px">Subject:<span class="fill"></span></div>
  <div class="row soft" style="top:355px">Task:<span class="fill"></span></div>
  <div class="row" style="top:379px">Subject:<span class="fill"></span></div>
  <div class="row soft" style="top:404px">Task:<span class="fill"></span></div>
  <div class="row" style="top:428px">Subject:<span class="fill"></span></div>
  <div class="row soft" style="top:453px">Task:<span class="fill"></span></div>
  <div class="row" style="top:477px">Subject:<span class="fill"></span></div>
  <div class="row soft" style="top:502px">Task:<span class="fill"></span></div>
  <div class="row" style="top:526px">Subject:<span class="fill"></span></div>
  <div class="row soft" style="top:551px">Task:<span class="fill"></span></div>
  <div class="row" style="top:575px">Subject:<span class="fill"></span></div>
  <div class="row soft" style="top:599px">Task:<span class="fill"></span></div>

  <div class="band" style="top:625px"><i style="left:0;width:133px"></i></div>

  <h2 class="heading" style="top:635px">
    <svg viewBox="0 0 20 20"><circle cx="10" cy="10" r="10" fill="var(--icon)"/><path d="M5.5 10.5l3 3 6-7" stroke="#fff" stroke-width="2.4" fill="none"/></svg>ASSESSMENTS
  </h2>
  <div class="row" style="top:659px">Assessment:<span class="fill short"></span><span class="due">Due</span><span class="fill"></span></div>
  <div class="row soft" style="top:684px">Element:<span class="fill"></span></div>
  <div class="row" style="top:708px">Assessment:<span class="fill short"></span><span class="due">Due</span><span class="fill"></span></div>
  <div class="row soft" style="top:733px">Element:<span class="fill"></span></div>
  <div class="row" style="top:757px">Assessment:<span class="fill short"></span><span class="due">Due</span><span class="fill"></span></div>
  <div class="row soft" style="top:782px">Element:<span class="fill"></span></div>
  <div class="row" style="top:806px">Assessment:<span class="fill short"></span><span class="due">Due</span><span class="fill"></span></div>
  <div class="row soft" style="top:831px">Element:<span class="fill"></span></div>
  <div class="row" style="top:855px">Assessment:<span class="fill short"></span><span class="due">Due</span><span class="fill"></span></div>
  <div class="row soft" style="top:880px">Element:<span class="fill"></span></div>
  <div class="row" style="top:904px">Assessment:<span class="fill short"></span><span class="due">Due</span><span class="fill"></span></div>
  <div class="row soft" style="top:928px">Element:<span class="fill"></span></div>

  <div class="band" style="top:967px"><i style="left:0;width:76px"></i><i style="left:477px;width:102px"></i></div>

  <h2 class="heading" style="top:977px">
    <svg viewBox="0 0 20 20"><circle cx="10" cy="10" r="10" fill="var(--icon)"/><rect x="6" y="5" width="8" height="10" fill="#fff"/><path d="M7.5 8h5M7.5 10h5M7.5 12h5" stroke="var(--icon)" stroke-width="1"/></svg>NOTES
  </h2>
  <h2 class="heading" style="top:977px;left:506px">
    <svg viewBox="0 0 20 20"><circle cx="10" cy="10" r="10" fill="var(--icon)"/><circle cx="8" cy="11" r="3" fill="none" stroke="#fff" stroke-width="1.6"/><circle cx="13" cy="8" r="2" fill="none" stroke="#fff" stroke-width="1.4"/></svg>PRACTICE
  </h2>
  <div class="vrule" style="left:393px;top:974px;height:128px"></div>
  <div class="vrule" style="left:212px;top:1000px;height:102px"></div>
  <div class="rule" style="left:30px;width:728px;top:1000px"></div>
  <div class="rule" style="left:30px;width:728px;top:1026px"></div>
  <div class="rule" style="left:30px;width:728px;top:1051px"></div>
  <div class="rule" style="left:30px;width:728px;top:1076px"></div>
  <div class="rule" style="left:30px;width:728px;top:1100px"></div>
  <span class="cell" style="left:39px;top:1003px">1.</span>
  <span class="cell" style="left:39px;top:1029px">2.</span>
  <span class="cell" style="left:39px;top:1054px">3.</span>
  <span class="cell" style="left:39px;top:1078px">4.</span>
  <span class="cell" style="left:223px;top:1003px">5.</span>
  <span class="cell" style="left:223px;top:1029px">6.</span>
  <span class="cell" style="left:223px;top:1054px">7.</span>
  <span class="cell" style="left:223px;top:1078px">8.</span>
</main>
</body>
</html>
```